Banner Ad Design Project

I place ads in Clickrow and also get traffic from sites like http://www.wellspringlistings.example.au/ to offer our free meditation CD and report at http://quietmindful.example.au/get-the-free-meditation-cd
We need new designs to improve this campaign.
Target Market(s)
40+ year old women, looking for personal growth or help with stress, depression, anxiety, sleep problems, health issues, memory/concentration issues
Industry/Entity Type
Campaign

```html
<!DOCTYPE html>
<html lang="en">
<head>
<meta charset="utf-8">
<title>Quiet Mindful – Banner Set</title>
<link rel="stylesheet" href="https://fonts.googleapis.com/css2?family=Arimo:wght@700&family=Roboto+Condensed:wght@700&display=swap">
<style>
  :root {
    --stage: #2b2b2b;
    --frame: #ffffff;
    --blue-light: #3d7fe0;
    --blue-dark: #1a4fb8;
    --orange: #f7870f;
    --ink: #111111;
    --paper: #ffffff;
    --disc-light: #e9eef4;
    --disc-dark: #7a9cc4;
  }
  * { margin: 0; padding: 0; box-sizing: border-box; }
  html, body { width: 1200px; height: 800px; overflow: hidden; background: var(--stage); }
  .stage { position: relative; width: 1200px; height: 800px; }

  .banner {
    position: absolute;
    border: 6px solid var(--frame);
    overflow: hidden;
    font-family: "Arimo", Arial, sans-serif;
  }
  .banner .shapes { position: absolute; inset: 0; width: 100%; height: 100%; display: block; }
  .banner .text { position: absolute; line-height: 1; white-space: nowrap; }

  .brand { color: var(--ink); font-weight: 700; font-family: "Arimo", Arial, sans-serif; }
  .offer { color: var(--paper); font-family: "Roboto Condensed", "Arial Narrow", sans-serif; font-weight: 700; text-shadow: 1px 1px 2px rgba(0,0,0,.35); }
  .headline-plain { color: var(--paper); font-family: "Arimo", Arial, sans-serif; font-weight: 700; text-shadow: 1px 1px 2px rgba(0,0,0,.35); }
  .price { color: var(--ink); font-weight: 700; }
  .price .amount { font-size: 1.75em; }

  .disc {
    position: absolute;
    border-radius: 50%;
    background: radial-gradient(circle at 50% 50%, #ffffff 0 9%, var(--disc-light) 10% 45%, var(--disc-dark) 100%);
    box-shadow: 0 1px 3px rgba(0,0,0,.4);
  }

  .skyscraper { left: 83px; top: 35px; width: 195px; height: 735px; }
  .rectangle { left: 445px; top: 50px; width: 430px; height: 360px; }
  .leaderboard-slim { left: 395px; top: 492px; width: 608px; height: 78px; }
  .leaderboard-wide { left: 333px; top: 630px; width: 748px; height: 133px; }
</style>
</head>
<body>
<main class="stage">

  <!-- Skyscraper -->
  <section class="banner skyscraper">
    <svg class="shapes" viewBox="0 0 183 723" preserveAspectRatio="none" aria-hidden="true">
      <defs>
        <linearGradient id="blue-sky" x1="0" y1="0" x2="1" y2="0">
          <stop offset="0" stop-color="var(--blue-dark)"/>
          <stop offset=".5" stop-color="var(--blue-light)"/>
          <stop offset="1" stop-color="var(--blue-dark)"/>
        </linearGradient>
      </defs>
      <rect width="183" height="723" fill="url(#blue-sky)"/>
      <path d="M0 0H183V106Q120 126 0 110Z" fill="var(--orange)"/>
      <path d="M0 0H183V97Q120 117 0 101Z" fill="var(--paper)"/>
      <path d="M0 582Q90 548 183 566V723H0Z" fill="var(--orange)"/>
    </svg>
    <div class="text brand" style="left:12px;top:20px;font-size:28px;">Quiet</div>
    <div class="text brand" style="left:12px;top:54px;font-size:28px;">Mindful</div>
    <div class="text offer" style="left:0;width:183px;text-align:center;top:162px;font-size:21px;">FREE Meditation CD</div>
    <div class="text offer" style="left:0;width:183px;text-align:center;top:192px;font-size:21px;">and Special Report</div>
    <div class="disc" role="img" aria-label="Meditation CD disc with a seated meditating woman" style="left:39px;top:244px;width:100px;height:100px;"></div>
    <div class="text offer" style="left:10px;top:416px;font-size:22px;">How to Meditate</div>
    <div class="text offer" style="left:37px;top:452px;font-size:22px;">Deeper Than</div>
    <div class="text offer" style="right:4px;top:489px;font-size:22px;">a Zen Monk!</div>
    <div class="text price" style="left:22px;top:604px;font-size:22px;">Valued</div>
    <div class="text price" style="left:92px;top:632px;font-size:22px;">at</div>
    <div class="text price" style="left:84px;top:662px;font-size:44px;">$37</div>
  </section>

  <!-- Medium rectangle -->
  <section class="banner rectangle">
    <svg class="shapes" viewBox="0 0 418 348" preserveAspectRatio="none" aria-hidden="true">
      <defs>
        <linearGradient id="blue-rect" x1="0" y1="0" x2="1" y2="1">
          <stop offset="0" stop-color="var(--blue-light)"/>
          <stop offset="1" stop-color="var(--blue-dark)"/>
        </linearGradient>
      </defs>
      <rect width="418" height="348" fill="url(#blue-rect)"/>
      <path d="M0 0H322Q302 86 150 99Q60 105 0 93Z" fill="var(--orange)"/>
      <path d="M0 0H306Q288 78 150 90Q60 96 0 86Z" fill="var(--paper)"/>
      <path d="M100 348Q200 268 418 262V348Z" fill="var(--orange)"/>
    </svg>
    <div class="text brand" style="left:26px;top:12px;font-size:30px;">Quiet</div>
    <div class="text brand" style="left:26px;top:48px;font-size:30px;">Mindful</div>
    <div class="disc" role="img" aria-label="Meditation CD disc with a seated meditating woman" style="left:286px;top:64px;width:90px;height:90px;"></div>
    <div class="text headline-plain" style="left:9px;top:116px;font-size:20px;">FREE Meditation CD</div>
    <div class="text headline-plain" style="left:16px;top:144px;font-size:20px;">and Special Report</div>
    <div class="text headline-plain" style="left:116px;top:182px;font-size:25px;">How to Meditate</div>
    <div class="text headline-plain" style="left:95px;top:217px;font-size:20px;">Deeper Than a Zen Monk!</div>
    <div class="text price" style="left:190px;top:296px;font-size:25px;">Value at <span class="amount">$37</span></div>
  </section>

  <!-- Slim leaderboard -->
  <section class="banner leaderboard-slim">
    <svg class="shapes" viewBox="0 0 596 66" preserveAspectRatio="none" aria-hidden="true">
      <defs>
        <linearGradient id="blue-slim" x1="0" y1="0" x2="0" y2="1">
          <stop offset="0" stop-color="var(--blue-light)"/>
          <stop offset="1" stop-color="var(--blue-dark)"/>
        </linearGradient>
      </defs>
      <rect width="596" height="66" fill="url(#blue-slim)"/>
      <path d="M0 0H182Q152 50 142 66H0Z" fill="var(--orange)"/>
      <path d="M0 0H172Q142 50 132 66H0Z" fill="var(--paper)"/>
      <path d="M420 66Q455 8 596 0V66Z" fill="var(--orange)"/>
    </svg>
    <div class="text brand" style="left:6px;top:3px;font-size:19px;">Quiet</div>
    <div class="text brand" style="left:6px;top:28px;font-size:19px;">Mindful</div>
    <div class="text offer" style="left:176px;top:8px;font-size:16px;">FREE Meditation CD and Special Report</div>
    <div class="text headline-plain" style="left:210px;top:30px;font-size:14px;">How to Meditate</div>
    <div class="text headline-plain" style="left:158px;top:48px;font-size:14px;">Deeper Than a Zen Monk!</div>
    <div class="text price" style="left:428px;top:28px;font-size:19px;">Value at <span class="amount">$37</span></div>
  </section>

  <!-- Wide leaderboard -->
  <section class="banner leaderboard-wide">
    <svg class="shapes" viewBox="0 0 736 121" preserveAspectRatio="none" aria-hidden="true">
      <defs>
        <linearGradient id="blue-wide" x1="0" y1="0" x2="1" y2="0">
          <stop offset="0" stop-color="var(--blue-dark)"/>
          <stop offset=".5" stop-color="var(--blue-light)"/>
          <stop offset="1" stop-color="var(--blue-dark)"/>
        </linearGradient>
      </defs>
      <rect width="736" height="121" fill="url(#blue-wide)"/>
      <path d="M0 0H250Q230 92 0 106Z" fill="var(--orange)"/>
      <path d="M0 0H238Q218 82 0 97Z" fill="var(--paper)"/>
      <path d="M450 121Q520 28 736 44V121Z" fill="var(--orange)"/>
    </svg>
    <div class="text brand" style="left:18px;top:14px;font-size:24px;">Quiet</div>
    <div class="text brand" style="left:18px;top:42px;font-size:24px;">Mindful</div>
    <div class="text offer" style="left:254px;top:19px;font-size:24px;">FREE Meditation CD and Special Report</div>
    <div class="text headline-plain" style="left:224px;top:69px;font-size:21px;">How to Meditate</div>
    <div class="text headline-plain" style="left:207px;top:97px;font-size:17px;">Deeper Than a Zen Monk!</div>
    <div class="text price" style="left:526px;top:73px;font-size:21px;">Valued at <span class="amount" style="font-size:2.2em;vertical-align:-6px;">$37</span></div>
  </section>

</main>
</body>
</html>
```